Website for my law practice

I am a solo practitioner, who specializes in family law and estate planning in Massachusetts. I need to re-do my website, as it is outdated. I like the idea of a nontraditional law firm website. My website address is: rosalindwhitcombelaw.com. I would like to retain my logo in the green color, as part of the new website. I have uploaded my logo below.

My hourly rate has changed from what is listed on my current website. My new hourly rate is $385.00. Please use this hourly rate when creating the website.

Good morning,

I have reviewed the designs submitted so far. I am happy that the "rw" logo in the green color is part of each of the designs submitted. I am also happy that the standard items seen in law firm websites, such as the scales of justice, etc. were not incorporated. Although the green logo is great, I do not think rest of the website has to have the same green color throughout. Additionally, I was hoping for something more creative, to make the website standout and not the stock web designs you see everyday. Please incorporate more unique images if you can. For example of what I mean, please look at this website: https://www.lucindaferrislaw.com

```html
<!DOCTYPE html>
<html lang="en">
<head>
<meta charset="utf-8">
<title>Rosalind Whitcombe, Attorney at Law</title>
<link rel="stylesheet" href="https://fonts.googleapis.com/css2?family=Josefin+Sans:wght@400;600;700&family=Poppins:wght@400;600;700&display=swap">
<style>
:root{
  --green:#4a8b37;
  --green-dark:#3d7a2c;
  --ink:#333333;
  --muted:#444444;
  --footer-bg:#e2eadf;
  --white:#ffffff;
}
*{margin:0;padding:0;box-sizing:border-box}
html,body{width:1200px;height:2370px;overflow:hidden}
body{font-family:"Poppins",sans-serif;color:var(--ink);background:var(--white);position:relative}
.heading{font-family:"Josefin Sans",sans-serif}
.topbar{position:absolute;left:0;top:0;width:1200px;height:45px;background:var(--green);color:var(--white);
  font-family:"Josefin Sans",sans-serif;font-size:17px;display:flex;justify-content:flex-end;align-items:center;gap:30px;padding-right:66px}
.topbar span{display:flex;align-items:center;gap:8px}
.topbar .call{font-size:19px;font-weight:600}
.header{position:absolute;left:0;top:45px;width:1200px;height:90px;background:var(--white)}
.brand{position:absolute;left:42px;top:22px;display:flex;align-items:center;gap:12px}
.brand-dot{width:44px;height:44px;border-radius:50%;background:var(--green)}
.brand-name{font-family:"Josefin Sans",sans-serif;font-weight:600;color:var(--green);font-size:18px;line-height:22px}
.nav{position:absolute;right:66px;top:40px;display:flex;gap:44px;font-family:"Josefin Sans",sans-serif;font-size:18px;color:#444}
.hero{position:absolute;left:0;top:135px;width:1200px;height:610px;
  background:radial-gradient(ellipse at 30% 35%,#c9c9c9 0,#8a8a86 18%,transparent 34%),
  radial-gradient(ellipse at 75% 60%,#6e7a5c 0,transparent 50%),
  linear-gradient(120deg,#5e6a4c,#7d7a62 40%,#56614a 70%,#3f4c35)}
.hero-title{position:absolute;left:650px;top:162px;color:var(--white);font-size:44px;line-height:46px;font-weight:400}
.btn-outline{position:absolute;border:2px solid var(--white);border-radius:30px;color:var(--white);
  font-family:"Josefin Sans",sans-serif;display:flex;align-items:center;justify-content:center}
.hero .btn-outline{left:651px;top:270px;width:255px;height:57px;background:var(--green);font-size:24px;padding-top:4px}
.hero-wave{position:absolute;left:0;top:540px}
.about-frame{position:absolute;left:356px;top:802px;width:156px;height:293px;border:2px solid var(--green);border-left:none}
.about-photo{position:absolute;left:166px;top:819px;width:320px;height:480px;
  background:linear-gradient(180deg,#8fb0c8 0,#7fa3bd 18%,#b99a72 40%,#c8a27e 60%,#8f8d78 85%,#7a7a6a 100%)}
.badge{position:absolute;left:94px;top:1114px;width:146px;height:146px;border-radius:50%;background:var(--white);
  box-shadow:0 6px 24px rgba(0,0,0,.18);display:flex;align-items:center;justify-content:center}
.badge-shape{width:86px;height:86px;border-radius:50%;background:#d9c27a}
.about-text{position:absolute;left:602px;top:818px;width:470px}
.about-text h2{font-size:44px;line-height:46px;font-weight:400;color:var(--ink)}
.about-text p{font-size:14px;line-height:22.5px;color:var(--muted);margin-top:20px}
.about-text h3{font-family:"Poppins",sans-serif;font-weight:600;color:var(--green);font-size:21px;margin-top:22px}
.about-text h3 + p{margin-top:24px}
.btn-solid{display:flex;align-items:center;justify-content:center;width:160px;height:56px;border-radius:28px;
  background:var(--green);color:var(--white);font-family:"Josefin Sans",sans-serif;font-weight:600;font-size:21px;margin-top:34px;padding-top:4px}
.consult{position:absolute;left:0;top:1438px;width:1200px;height:482px;
  background:linear-gradient(90deg,#4a8b37 0,#4b8a39 55%,#427d32 100%)}
.consult h2{position:absolute;left:93px;top:110px;color:var(--white);font-size:42px;font-weight:400}
.consult p{position:absolute;left:93px;top:185px;width:530px;color:var(--white);font-size:14px;line-height:22.5px}
.consult .btn-outline{left:95px;top:298px;width:367px;height:58px;font-size:25px;padding-top:4px}
.footer{position:absolute;left:0;top:1920px;width:1200px;height:450px;background:var(--footer-bg)}
.footer .brand{left:136px;top:175px}
.copy{position:absolute;left:133px;top:282px;font-family:"Josefin Sans",sans-serif;font-size:18px;color:#222}
.divider{position:absolute;top:85px;width:2px;height:305px;background:var(--green)}
.col-title{position:absolute;top:98px;font-family:"Josefin Sans",sans-serif;font-weight:600;color:var(--green);font-size:32px}
.contact-item{position:absolute;left:508px;display:flex;align-items:center;gap:14px;font-family:"Josefin Sans",sans-serif;font-size:18px;line-height:22px;color:#222}
.icon{width:46px;height:46px;border-radius:50%;background:var(--green);border:3px solid var(--white);
  box-shadow:0 0 0 1px #cfdccb;display:flex;align-items:center;justify-content:center;flex:none}
.links{position:absolute;left:944px;top:160px;list-style:none;font-family:"Josefin Sans",sans-serif;font-size:18px;color:#222}
.links li{height:32px}
</style>
</head>
<body>
<div class="topbar">
  <span><svg width="13" height="10" viewBox="0 0 13 10"><rect width="13" height="10" rx="1" fill="#fff"/><path d="M0 1l6.5 4.5L13 1" stroke="#4a8b37" stroke-width="1.4" fill="none"/></svg>rosalindwhitcombe@mail.com</span>
  <span class="call"><svg width="14" height="14" viewBox="0 0 24 24"><path fill="#fff" d="M6.6 10.8a15 15 0 006.6 6.6l2.2-2.2c.3-.3.7-.4 1-.2 1.1.4 2.3.6 3.6.6.6 0 1 .4 1 1V20c0 .6-.4 1-1 1A17 17 0 013 4c0-.6.4-1 1-1h3.5c.6 0 1 .4 1 1 0 1.3.2 2.5.6 3.6.1.3 0 .7-.2 1z"/></svg>Call: (978)555-0142</span>
</div>

<header class="header">
  <div class="brand"><span class="brand-dot"></span><span class="brand-name">Rosalind Whitcombe<br>Attorney at Law</span></div>
  <nav class="nav"><span>Home</span><span>Family Law</span><span>Estate Planning</span><span>About</span><span>Location</span><span>Contact</span><span>FAQ</span></nav>
</header>

<section class="hero" role="img" aria-label="Black and white portrait of the attorney over a soft-focus garden of greenery">
  <h1 class="hero-title heading">Rosalind Whitcombe<br>Attorney at Law</h1>
  <span class="btn-outline">Free Consultation</span>
  <svg class="hero-wave" width="1200" height="200" viewBox="0 0 1200 200">
    <path d="M0 12 C120 60 300 95 560 93 C820 92 1060 110 1200 200 L1200 200 L0 200 Z" fill="#ffffff"/>
    <path d="M0 18 C140 70 320 92 560 95 C840 98 1060 120 1200 198" stroke="#4a8b37" stroke-width="2" fill="none"/>
    <path d="M0 20 C140 60 330 85 560 92 C300 90 150 95 0 185 Z" fill="#4a8b37"/>
    <path d="M900 100 C1030 110 1140 140 1200 160 L1200 120 C1110 105 1000 100 900 100 Z" fill="#4a8b37"/>
  </svg>
</section>

<div class="about-frame"></div>
<div class="about-photo" role="img" aria-label="Portrait of the attorney smiling outdoors by the sea"></div>
<div class="badge" role="img" aria-label="Client satisfaction award badge"><span class="badge-shape"></span></div>

<section class="about-text">
  <h2 class="heading">Rosalind Whitcombe,<br>Attorney at Law</h2>
  <p>Rosalind Whitcombe is a Solo Practitioner focusing her practice on matters pertaining to family law and estate planning.</p>
  <h3>Close, Personal Representation</h3>
  <p>When I am retained, my clients are my priority. As a result, I work closely with each one to keep them informed through each step of the legal proceeding. Clients have always expressed to me how frustrating it is when attorneys don’t return phone calls. I understand this, as I am often met with the same challenges in the profession. I am proud of my practice and my reputation, and I return calls promptly.</p>
  <span class="btn-solid">Read More</span>
</section>

<section class="consult" role="img" aria-label="Green-tinted photo of hands working at a laptop">
  <h2 class="heading">Free 30-Minute Consultation</h2>
  <p>I respect the fact that your time is valuable. Therefore, I provide a free 30 minute consultation to potential clients. The consultation is a great way to learn more about what options there are for your issue, as well as for both you and I to see if we are a good fit.</p>
  <span class="btn-outline">Book A Free Consultation</span>
</section>

<footer class="footer">
  <div class="brand"><span class="brand-dot"></span><span class="brand-name">Rosalind Whitcombe<br>Attorney at Law</span></div>
  <p class="copy">© 2025 All Rights are Reserved.</p>
  <span class="divider" style="left:453px"></span>
  <span class="divider" style="left:885px"></span>
  <h3 class="col-title" style="left:507px">Contact</h3>
  <div class="contact-item" style="top:150px"><span class="icon"><svg width="16" height="20" viewBox="0 0 16 20"><path fill="#fff" d="M8 0a8 8 0 00-8 8c0 6 8 12 8 12s8-6 8-12a8 8 0 00-8-8zm0 11a3 3 0 110-6 3 3 0 010 6z"/></svg></span><span>42 Linden Street<br>Beverly, MA 01915</span></div>
  <div class="contact-item" style="top:240px"><span class="icon"><svg width="18" height="18" viewBox="0 0 24 24"><path fill="#fff" d="M6.6 10.8a15 15 0 006.6 6.6l2.2-2.2c.3-.3.7-.4 1-.2 1.1.4 2.3.6 3.6.6.6 0 1 .4 1 1V20c0 .6-.4 1-1 1A17 17 0 013 4c0-.6.4-1 1-1h3.5c.6 0 1 .4 1 1 0 1.3.2 2.5.6 3.6.1.3 0 .7-.2 1z"/></svg></span><span>Phone: 978-555-0142<br>Fax: 978-555-0143</span></div>
  <div class="contact-item" style="top:332px"><span class="icon"><svg width="18" height="13" viewBox="0 0 13 10"><rect width="13" height="10" rx="1" fill="#fff"/><path d="M0 1l6.5 4.5L13 1" stroke="#4a8b37" stroke-width="1.4" fill="none"/></svg></span><span>Emial:<br>rosalindwhitcombe@mail.com</span></div>
  <h3 class="col-title" style="left:943px">Links</h3>
  <ul class="links"><li>Home</li><li>Family Law</li><li>Estate Planning</li><li>About</li><li>Location</li><li>Contact</li><li>FAQ</li></ul>
</footer>
</body>
</html>
```